I need a book cover (front and back) for a book I wrote called "7 Habits of Dress: A Closet Map for Growth".

The short version of the book can be found online here: https://filebinder.example/doc/7QkZ-pLm3Rt8yXvB2NcWd9HsJf4GaE/open

I'm working on expanding this into a real book (100+ pages, with images), and putting it on Brindlo.

I'm the author, Milo Vashenko. I was named "Finest Groomed Gent in America" by Dapperline Journal, and I would like to add that to the cover for credibility.

My website "About Page" has more info about me and my business Threads of Merit: https://threadsofmerit.example/pages/about-us

I also attached the first version of the cover I made using Canva.

I have LOTS of images, if you need some (mannequins, models, garments, etc). See our website's blog for more ideas of the images we have: https://threadsofmerit.example/blogs/news

```html
<!DOCTYPE html>
<html lang="en">
<head>
<meta charset="utf-8">
<title>7 Habits of Dress – Book Cover</title>
<link rel="stylesheet" href="https://fonts.googleapis.com/css2?family=Playfair+Display:wght@400;500;600&family=Jost:wght@400;500;600&display=swap">
<style>
  :root {
    --backdrop: #545454;
    --cover-black: #151515;
    --spine-black: #1b1b1b;
    --gold: #c7ab7f;
    --cream: #ecebe6;
    --body-text: #d9d9d6;
    --photo-dark: #1a1512;
    --photo-mid: #3a2c22;
    --photo-light: #6a5744;
  }
  * { box-sizing: border-box; margin: 0; padding: 0; }
  html, body {
    width: 1200px; height: 740px; overflow: hidden;
    background: var(--backdrop);
  }
  .wrap {
    position: absolute; left: 105px; top: 30px;
    width: 990px; height: 680px;
    display: flex;
  }

  /* ---------- back cover ---------- */
  .back {
    position: relative; width: 460px; height: 680px;
    background: var(--cover-black);
    font-family: "Jost", sans-serif;
    color: var(--body-text);
  }
  .back-copy {
    position: absolute; left: 66px; top: 116px; width: 330px;
    font-size: 8.1px; line-height: 1.36; text-align: justify;
  }
  .mini-title {
    float: left; width: 72px; margin: -2px 8px 2px 0;
    font-family: "Playfair Display", serif; line-height: 0.9; color: var(--cream);
  }
  .mini-title .num { display: block; font-size: 56px; color: var(--gold); line-height: 0.82; }
  .mini-title .word { display: block; font-size: 21px; letter-spacing: -0.5px; }
  .mini-title .small { display: block; font-size: 11px; padding-left: 22px; line-height: 0.8; }
  .tagline {
    font-weight: 600; font-size: 11px; color: var(--gold); margin-bottom: 2px; text-align: left;
  }
  .back-copy p { margin-bottom: 6px; }
  .end-mark {
    display: inline-block; width: 3px; height: 10px; background: var(--gold);
    vertical-align: -2px; margin-left: 4px;
  }
  .portrait {
    position: absolute; left: 163px; top: 318px;
    width: 134px; height: 134px; border-radius: 50%;
    border: 1.5px solid var(--gold);
    padding: 4px;
  }
  .portrait-fill {
    width: 100%; height: 100%; border-radius: 50%;
    background: radial-gradient(circle at 50% 40%, #5e6670 0%, #363c44 55%, #1e232a 100%);
  }
  .bio {
    position: absolute; left: 66px; top: 468px; width: 330px;
    font-size: 8.1px; line-height: 1.36; text-align: justify;
  }
  .bio p { margin-bottom: 6px; }

  /* ---------- spine ---------- */
  .spine {
    position: relative; width: 70px; height: 680px;
    background: var(--spine-black);
    border-left: 1px solid #0c0c0c; border-right: 1px solid #0c0c0c;
    display: flex; justify-content: center; padding-top: 100px;
  }
  .spine-text {
    writing-mode: vertical-rl;
    display: flex; align-items: center;
  }
  .spine-title {
    font-family: "Playfair Display", serif; font-size: 44px; color: var(--gold);
    letter-spacing: -1px; line-height: 1;
  }
  .spine-title .small { font-size: 22px; }
  .spine-rule { width: 1px; height: 1px; }
  .spine-divider {
    display: block; inline-size: 1.5px; block-size: 36px;
    background: var(--gold); margin: 0 6px 0 8px;
  }
  .spine-author {
    font-family: "Jost", sans-serif; font-weight: 500; font-size: 18px;
    letter-spacing: 4px; color: var(--cream);
  }

  /* ---------- front cover ---------- */
  .front {
    position: relative; width: 460px; height: 680px; overflow: hidden;
    background: var(--cover-black);
  }
  .front-photo {
    position: absolute; inset: 0;
    background:
      radial-gradient(ellipse 50% 55% at 58% 48%, rgba(70,86,130,0.55) 0%, rgba(0,0,0,0) 70%),
      linear-gradient(180deg, var(--photo-dark) 0%, var(--photo-mid) 45%, var(--photo-light) 78%, var(--photo-mid) 100%);
  }
  .accolade {
    position: absolute; left: 0; right: 0; top: 30px; text-align: center;
    font-family: "Jost", sans-serif; font-size: 10.5px; color: var(--cream);
  }
  .accolade::before, .accolade::after {
    content: ""; position: absolute; left: 150px; width: 166px; height: 1px; background: #9b9b96;
  }
  .accolade::before { top: -9px; }
  .accolade::after { bottom: -8px; }
  .big-numeral {
    position: absolute; left: 130px; top: 20px;
    font-family: "Playfair Display", serif; font-weight: 500;
    font-size: 380px; line-height: 1; color: var(--gold);
  }
  .front-title {
    position: absolute; left: 0; right: 0; top: 390px; text-align: right; padding-right: 38px;
    font-family: "Playfair Display", serif; color: var(--cream); line-height: 0.88;
  }
  .front-title .word { display: block; font-size: 84px; letter-spacing: -2px; }
  .front-title .small { display: block; font-size: 40px; padding-right: 100px; line-height: 0.7; }
  .subtitle {
    position: absolute; left: 122px; top: 620px;
    font-family: "Jost", sans-serif; font-size: 14px; color: var(--cream);
  }
  .author {
    position: absolute; left: 0; right: 0; top: 640px; text-align: center;
    font-family: "Jost", sans-serif; font-weight: 600; font-size: 21px;
    letter-spacing: 5px; color: var(--cream);
  }
</style>
</head>
<body>
<div class="wrap">

  <section class="back">
    <div class="back-copy">
      <div class="mini-title">
        <span class="num">7</span>
        <span class="word">Habits</span>
        <span class="small">of</span>
        <span class="word">Dress</span>
      </div>
      <div class="tagline">Style is not vanity. It's strategy.</div>
      <p>Like it or not, the way you dress has a huge impact on your life. It doesn't matter how smart you are or how good you are at your job; if people assume you are sloppy and can't be trusted, you're fighting an uphill battle. Most people are climbing this mountain and don't understand why progress is so hard to make - professionally, socially, romantically, or otherwise.</p>
      <p>The good news is - like any other skill - style is something you can learn, practice and improve.</p>
      <p>This book will give you a foundation for understanding how to dress for success and build a lasting wardrobe that works for you. I've used these principles to help thousands of people get raises and promotions, meet their future wives, become the leader of their social circles and significantly improve their confidence.<span class="end-mark"></span></p>
    </div>

    <div class="portrait">
      <div class="portrait-fill" role="img" aria-label="Author portrait photograph"></div>
    </div>

    <div class="bio">
      <p>Milo Vashenko was named “America's Finest Groomed Gent” by Dapperline Journal while studying psychology - and playing basketball - at Halverton University. He then trained to become a bespoke tailor, earned a degree in Menswear Design from the Meridian Institute of Design in NYC and started a menswear blog that gained millions of readers worldwide.</p>
      <p>After 10 years of working with customers in-person in New York City, Milo combined his experience in bespoke tailoring with his passion for teaching men how to dress for success and expanded his award-winning blog into Threads of Merit; a full-service online bespoke tailor shop.</p>
      <p>Today Milo lives in Toronto with his wife Lena and their daughter Mira where he meets with customers on Vidloop from all over the world to refine their style and build their dream wardrobes.<span class="end-mark"></span></p>
    </div>
  </section>

  <section class="spine">
    <div class="spine-text">
      <span class="spine-title">7 Habits <span class="small">of</span> Dress</span>
      <span class="spine-divider"></span>
      <span class="spine-author">MILO VASHENKO</span>
    </div>
  </section>

  <section class="front">
    <div class="front-photo" role="img" aria-label="Photograph of the author standing in a blue double-breasted suit in a dim brick-walled room"></div>
    <div class="accolade">“Finest Groomed Gent in America” by Dapperline Journal</div>
    <div class="big-numeral">7</div>
    <h1 class="front-title">
      <span class="word">Habits</span>
      <span class="small">of</span>
      <span class="word">Dress</span>
    </h1>
    <div class="subtitle">A Closet Map for Growth</div>
    <div class="author">MILO VASHENKO</div>
  </section>

</div>
</body>
</html>
```